Business Card Design Project

I want a new business card for all 5 of my companies. Card needs to be double sided with my name and details on one side and all 5 logos on the other side.

Industry/Entity Type

Business

```html
<!DOCTYPE html>
<html lang="en">
<head>
<meta charset="utf-8">
<title>Tallbrace Business Card</title>
<link rel="stylesheet" href="https://fonts.googleapis.com/css2?family=Archivo:wght@400;800&display=swap">
<style>
  :root {
    --page: #ecebe8;
    --card-white: #ffffff;
    --panel-light: #f4f4f4;
    --panel-shade: #e4e4e4;
    --stripe-grey: #e0e0e0;
    --stripe-white: #fbfbfb;
    --stripe-ice: #dde6ec;
    --edge-blue: #1c9ad6;
    --edge-black: #0d0d0d;
    --ink: #111111;
  }
  * { margin: 0; padding: 0; box-sizing: border-box; }
  html, body { width: 1200px; height: 1024px; overflow: hidden; }
  body {
    background: var(--page);
    font-family: "Archivo", "Arial", sans-serif;
    display: flex;
    flex-direction: column;
    align-items: center;
    justify-content: center;
    gap: 64px;
  }
  .card {
    position: relative;
    width: 720px;
    height: 412px;
    background: var(--card-white);
    overflow: hidden;
    box-shadow: 0 6px 22px rgba(0,0,0,0.12);
  }
  .stripes { position: absolute; inset: 0; display: flex; }
  .stripe { flex: 1; }
  .stripe--ice { background: var(--stripe-ice); }
  .stripe--grey { background: var(--stripe-grey); }
  .stripe--white { background: var(--stripe-white); }

  .details-panel {
    position: absolute;
    left: 0; top: 0; bottom: 0;
    width: 420px;
    background: linear-gradient(135deg, var(--card-white) 0%, var(--panel-light) 55%, var(--panel-shade) 100%);
    padding: 96px 0 0 64px;
    color: var(--ink);
    box-shadow: 2px 0 8px rgba(0,0,0,0.06);
  }
  .brand-name { font-weight: 800; font-size: 24px; letter-spacing: 0.5px; line-height: 1.05; }
  .detail-line { font-size: 15px; line-height: 1.25; letter-spacing: 0.4px; text-transform: uppercase; white-space: nowrap; }
  .detail-group { margin-bottom: 14px; }
  .detail-group.address { padding-left: 18px; }
  .detail-group.contact { padding-left: 36px; }
  .detail-group.online { padding-left: 54px; }

  .logo-row {
    position: absolute;
    inset: 0;
    display: flex;
  }
  .company-mark {
    flex: 1;
    display: flex;
    flex-direction: column;
    align-items: center;
    justify-content: center;
    gap: 12px;
  }
  .company-mark__square { width: 28px; height: 28px; background: var(--edge-blue); }
  .company-mark__name {
    font-weight: 800;
    font-size: 13px;
    letter-spacing: 0.6px;
    color: var(--ink);
    text-align: center;
    line-height: 1.2;
  }

  .edge-marks { position: absolute; left: 0; width: 100%; height: 14px; display: flex; justify-content: space-between; }
  .edge-marks--bottom { bottom: 0; }
  .edge-marks--top { top: 0; }
  .edge-set { display: flex; }
  .mark-blue { width: 44px; background: var(--edge-blue); }
  .mark-black { width: 90px; background: var(--edge-black); }
</style>
</head>
<body>

  <section class="card card--front" aria-label="Card front">
    <div class="stripes">
      <div class="stripe stripe--ice"></div>
      <div class="stripe stripe--grey"></div>
      <div class="stripe stripe--white"></div>
      <div class="stripe stripe--grey"></div>
      <div class="stripe stripe--ice"></div>
    </div>
    <div class="details-panel">
      <div class="detail-group">
        <div class="brand-name">TALLBRACE</div>
        <div class="detail-line">Harbourview Scaffold Hire</div>
      </div>
      <div class="detail-group address">
        <div class="detail-line">24 Orchard Lane,</div>
        <div class="detail-line">Brightvale SA 5099</div>
      </div>
      <div class="detail-group contact">
        <div class="detail-line">(08) 8412 5570</div>
        <div class="detail-line">0451 306 918</div>
      </div>
      <div class="detail-group online">
        <div class="detail-line">office@tallbrace.com.au</div>
        <div class="detail-line">www.tallbrace.com.au</div>
      </div>
    </div>
    <div class="edge-marks edge-marks--bottom">
      <div class="edge-set"><span class="mark-blue"></span><span class="mark-black"></span></div>
      <div class="edge-set"><span class="mark-black"></span><span class="mark-blue"></span></div>
    </div>
  </section>

  <section class="card card--back" aria-label="Card back with five company names">
    <div class="stripes">
      <div class="stripe stripe--ice"></div>
      <div class="stripe stripe--grey"></div>
      <div class="stripe stripe--white"></div>
      <div class="stripe stripe--grey"></div>
      <div class="stripe stripe--ice"></div>
    </div>
    <div class="logo-row">
      <div class="company-mark"><span class="company-mark__square"></span><span class="company-mark__name">TALLBRACE</span></div>
      <div class="company-mark"><span class="company-mark__square"></span><span class="company-mark__name">HARBOURVIEW<br>HIRE</span></div>
      <div class="company-mark"><span class="company-mark__square"></span><span class="company-mark__name">RIDGELINE<br>ACCESS</span></div>
      <div class="company-mark"><span class="company-mark__square"></span><span class="company-mark__name">STEELPOINT<br>FORMWORK</span></div>
      <div class="company-mark"><span class="company-mark__square"></span><span class="company-mark__name">KESTREL<br>SITE SUPPLY</span></div>
    </div>
    <div class="edge-marks edge-marks--top">
      <div class="edge-set"><span class="mark-blue"></span><span class="mark-black"></span></div>
      <div class="edge-set"><span class="mark-black"></span><span class="mark-blue"></span></div>
    </div>
  </section>

</body>
</html>
```